Whitcombe Framing Works - Card Design

I am looking to use the logo designs that you already did for me to develop a business card. I would like the card to have a black background and be double sided. I want white and green logo and text. I have attached an inspiration photo of a look that I like. I would like to use the Vertical Logo attached to take up the full front side of the card. On the back where I have my name and information, I would like to have the horizontal logo or maybe even just the image of the 'A' and trees without the text. I am open, but I am looking for something clean and simple and I want the green to really pop! Additional files can be found under Design #: 40593216

Target Market(s)

Homeowners

Industry/Entity Type

Construction

Contact Information for Business Card

Name: Marcus Pellow, Title: Project Manager, Phone: 831.555.0147, Email: whitcombeframingworks@mailbarn.net, address: 418 Juniper Ln, Felton, CA 95092, Lic# 2046318

Colors
00AB8E
00BBA5
67D7C9
C6EFE9
E9F9F6

Requirements
Nice to have
• I would like to see the logos that I have already got from SketchHarbor, though I am open to new ones

```html
<!DOCTYPE html>
<html lang="en">
<head>
<meta charset="utf-8">
<title>Whitcombe Framing Works – Business Card</title>
<link href="https://fonts.googleapis.com/css2?family=Montserrat:wght@400;500;700&display=swap" rel="stylesheet">
<style>
  :root {
    --backdrop: #3a3431;
    --card: #1d1d1e;
    --card-edge: #262627;
    --green: #5cbf3b;
    --white: #f4f4f4;
    --muted: #d9d9d9;
  }
  * { margin: 0; padding: 0; box-sizing: border-box; }
  html, body {
    width: 1200px; height: 786px; overflow: hidden;
    background: var(--backdrop);
    font-family: "Montserrat", Arial, sans-serif;
  }
  .stage {
    position: relative; width: 1200px; height: 786px;
  }
  .card {
    position: absolute; top: 238px;
    width: 540px; height: 309px;
    background: linear-gradient(135deg, var(--card-edge), var(--card));
    border-radius: 4px;
    box-shadow: 0 10px 30px rgba(0,0,0,.45);
    overflow: hidden;
  }
  .card--details { left: 40px; }
  .card--brand { left: 620px; }

  /* wordmark */
  .wordmark {
    display: flex; align-items: center; gap: 12px;
    color: var(--white); font-weight: 700;
    text-transform: uppercase; letter-spacing: 1.5px; line-height: 1.05;
  }
  .wordmark__square {
    flex: none; width: 30px; height: 30px; background: var(--green);
  }
  .card--details .wordmark {
    position: absolute; left: 34px; top: 40px; font-size: 21px;
  }
  .card--brand .wordmark {
    position: absolute; left: 0; right: 0; top: 50%;
    transform: translateY(-50%); justify-content: center; font-size: 27px;
  }
  .card--brand .wordmark__square { width: 38px; height: 38px; }

  .divider {
    position: absolute; left: 34px; right: 34px; top: 142px;
    height: 2px; background: var(--green);
  }
  .licence {
    position: absolute; right: 34px; top: 116px;
    font-size: 12px; font-weight: 500; color: var(--white);
  }
  .licence__label { color: var(--green); }

  .person { position: absolute; left: 34px; top: 162px; }
  .person__name {
    font-size: 22px; font-weight: 700; color: var(--green); line-height: 1.1;
  }
  .person__title {
    font-size: 13px; color: var(--white); margin-top: 3px;
  }
  .contact {
    position: absolute; left: 34px; top: 222px;
    list-style: none; font-size: 12.5px; color: var(--muted);
  }
  .contact__item {
    display: flex; align-items: center; gap: 10px; height: 22px;
  }
  .contact__icon { width: 12px; height: 12px; fill: var(--green); flex: none; }
</style>
</head>
<body>
<main class="stage">
  <section class="card card--details" aria-label="Business card, contact side">
    <div class="wordmark">
      <span class="wordmark__square"></span>
      <span>Whitcombe<br>Framing Works</span>
    </div>
    <p class="licence"><span class="licence__label">Lic</span> #2046318</p>
    <div class="divider"></div>
    <div class="person">
      <p class="person__name">Marcus Pellow</p>
      <p class="person__title">Project Manager</p>
    </div>
    <ul class="contact">
      <li class="contact__item">
        <svg class="contact__icon" viewBox="0 0 12 12"><path d="M6 0a4 4 0 0 0-4 4c0 3 4 8 4 8s4-5 4-8a4 4 0 0 0-4-4zm0 5.6A1.6 1.6 0 1 1 6 2.4a1.6 1.6 0 0 1 0 3.2z"/></svg>
        418 Juniper Ln, Felton, CA 95092
      </li>
      <li class="contact__item">
        <svg class="contact__icon" viewBox="0 0 12 12"><path d="M2.5 0.5l2 2.2-1.1 1.6c.8 1.6 2.1 2.9 3.7 3.7l1.6-1.1 2.2 2-1 2.4C4.6 11 1 7.4.1 1.5z"/></svg>
        831.555.0147
      </li>
      <li class="contact__item">
        <svg class="contact__icon" viewBox="0 0 12 12"><path d="M0 2h12v8H0zM1 3l5 3.5L11 3v-.2H1z" fill-rule="evenodd"/></svg>
        whitcombeframingworks@mailbarn.net
      </li>
    </ul>
  </section>

  <section class="card card--brand" aria-label="Business card, brand side">
    <div class="wordmark">
      <span class="wordmark__square"></span>
      <span>Whitcombe<br>Framing Works</span>
    </div>
  </section>
</main>
</body>
</html>
```